New boutique IT consultancy needs business card

I need a business card and logo for my IT consultancy business, called 'Quenmarlo' . I want it to make me look bigger than I am. I want it to look classy, and modern. Simple design, that will be easy for me to translate into my webpage etc. The business card should be bold, and different.

The logo should emphasise the 'y' as used in quenmarlo

Target Market(s)

IT divisions in other companies

Industry/Entity Type

Business

Contact Information for Business Card

Doreen Pakfield
Director
+61 437 918 205
dpakfield@quenmarlo-mail.test

```html
<!DOCTYPE html>
<html lang="en">
<head>
<meta charset="utf-8">
<title>Quenmarlo — Business Card</title>
<link rel="stylesheet" href="https://fonts.googleapis.com/css2?family=Kanit:wght@300;400;500&display=swap">
<style>
  :root {
    --backdrop: #e9e4df;
    --card-white: #ffffff;
    --ink: #231f20;
    --band-dark: #231f20;
    --stripe-dark: #2b2829;
    --accent: #f05a28;
    --icon-grey: #8a8a8a;
    --text: #1e1e1e;
  }
  * { margin: 0; padding: 0; box-sizing: border-box; }
  html, body { width: 1200px; height: 799px; overflow: hidden; }
  body {
    background: var(--backdrop);
    font-family: "Kanit", sans-serif;
    position: relative;
  }
  .card {
    position: absolute;
    top: 272px;
    width: 460px;
    height: 256px;
    background: var(--card-white);
    box-shadow: 0 2px 6px rgba(0,0,0,0.25);
    overflow: hidden;
  }
  .card--front { left: 120px; }
  .card--back { left: 620px; }

  /* Front */
  .front__band {
    position: absolute; left: 0; right: 0;
    background: var(--band-dark);
  }
  .front__band--top { top: 0; height: 59px; }
  .front__band--bottom { bottom: 0; height: 56px; }
  .brand {
    position: absolute; left: 0; right: 0; top: 59px; bottom: 56px;
    display: flex; align-items: center; justify-content: center; gap: 14px;
  }
  .brand__mark {
    width: 18px; height: 18px; background: var(--accent);
  }
  .brand__name {
    font-size: 46px; font-weight: 500; letter-spacing: 4px;
    text-transform: uppercase; color: var(--ink); line-height: 1;
  }

  /* Back */
  .back__stripe {
    position: absolute; left: 0; top: 0; bottom: 0; width: 49px;
    background: var(--stripe-dark);
  }
  .back__nametab {
    position: absolute; right: 0; top: 20px; width: 232px; height: 61px;
    background: var(--accent);
    clip-path: polygon(0 0, 100% 0, 100% 100%, 18% 100%);
    color: var(--card-white);
  }
  .back__name {
    position: absolute; left: 45px; top: 8px;
    font-size: 17px; font-weight: 300; letter-spacing: 0.5px;
    text-transform: uppercase; white-space: nowrap;
  }
  .back__name strong { font-weight: 500; }
  .back__title {
    position: absolute; left: 45px; top: 32px;
    font-size: 11px; font-weight: 300;
  }
  .contact {
    position: absolute; left: 33px;
    display: flex; align-items: center; gap: 16px;
    font-size: 15px; font-weight: 300; color: var(--text);
  }
  .contact--phone { top: 98px; }
  .contact--email { top: 149px; }
  .contact__icon {
    width: 32px; height: 32px; background: var(--icon-grey);
    display: flex; align-items: center; justify-content: center;
  }
  .contact__icon svg { width: 18px; height: 18px; }
</style>
</head>
<body>
  <section class="card card--front" aria-label="Card front">
    <div class="front__band front__band--top"></div>
    <div class="brand">
      <span class="brand__mark"></span>
      <span class="brand__name">Quenmarlo</span>
    </div>
    <div class="front__band front__band--bottom"></div>
  </section>

  <section class="card card--back" aria-label="Card back">
    <div class="back__stripe"></div>
    <div class="back__nametab">
      <p class="back__name">Doreen <strong>Pakfield</strong></p>
      <p class="back__title">Director</p>
    </div>
    <div class="contact contact--phone">
      <span class="contact__icon">
        <svg viewBox="0 0 24 24" fill="#ffffff" aria-hidden="true">
          <path d="M6.6 10.8c1.4 2.8 3.8 5.1 6.6 6.6l2.2-2.2c.3-.3.7-.4 1-.2 1.1.4 2.3.6 3.6.6.6 0 1 .4 1 1V20c0 .6-.4 1-1 1C10.6 21 3 13.4 3 4c0-.6.4-1 1-1h3.5c.6 0 1 .4 1 1 0 1.3.2 2.5.6 3.6.1.3 0 .7-.2 1z"/>
        </svg>
      </span>
      <span class="contact__text">+61 437 918 205</span>
    </div>
    <div class="contact contact--email">
      <span class="contact__icon">
        <svg viewBox="0 0 24 24" fill="none" stroke="#ffffff" stroke-width="2" aria-hidden="true">
          <circle cx="12" cy="12" r="9"/>
          <ellipse cx="12" cy="12" rx="4" ry="9"/>
          <line x1="3" y1="12" x2="21" y2="12"/>
        </svg>
      </span>
      <span class="contact__text">dpakfield@quenmarlo-mail.test</span>
    </div>
  </section>
</body>
</html>
```